Logistics Website Design

See website https://tvarfreightglobal.com for theme and color details. Need the site to be re-done and reflect some of the designs shown in this list here: https://pinvora.com/tags/logistics-company-website

Target Market(s)

Logistics & Transportation

Industry/Entity Type

Logistics and Supply Chain

Coding

Coded - Design and coding required

Number of Pages Required

5+ page

Requirements
Must have
• Colors must match theme of logo. Looking for a sleek, interactive design.

```html
<!DOCTYPE html>
<html lang="en">
<head>
<meta charset="utf-8">
<title>Tvar Freight Global — Logistics</title>
<link rel="stylesheet" href="https://fonts.googleapis.com/css2?family=Montserrat:wght@300;400;500;600;800;900&display=swap">
<style>
:root{
  --orange:#e85d2c;
  --orange-soft:#f6e2dc;
  --brown:#4a1a0c;
  --brown-deep:#3b1409;
  --page:#f5f1ef;
  --band:#e5dcd8;
  --text:#3d2a24;
  --muted:#6b5a54;
  --line:#d9a896;
  --white:#ffffff;
  --star:#f5a623;
}
*{box-sizing:border-box;margin:0;padding:0}
html,body{width:1200px;height:3425px;overflow:hidden}
body{font-family:'Montserrat',sans-serif;background:var(--page);color:var(--text);position:relative}
.abs{position:absolute}
.btn{position:absolute;background:var(--orange);color:var(--white);font-size:15px;font-weight:500;display:flex;align-items:center;justify-content:center;border-radius:3px;text-decoration:none}
.brand{display:flex;align-items:center;gap:10px;font-weight:800;font-size:17px;letter-spacing:.5px;color:var(--white)}
.brand-dot{width:40px;height:40px;border-radius:50%;background:var(--orange)}

/* hero */
.hero{position:absolute;left:0;top:0;width:1200px;height:642px;background:linear-gradient(180deg,#8f9aa6 0%,#7b8591 45%,#9a9ea3 75%,#c9cacb 100%)}
.hero-photo{position:absolute;inset:0;background:radial-gradient(ellipse at 78% 45%,#e8eaec 0%,#c8ccd0 22%,rgba(120,130,140,0) 55%)}
.hero .brand{position:absolute;left:112px;top:56px}
.nav{position:absolute;left:471px;top:46px;display:flex;gap:27px;font-size:15px;color:var(--white)}
.nav .active{font-weight:600;text-decoration:underline;text-underline-offset:6px}
.hero-title{position:absolute;left:112px;top:196px;color:var(--white);font-size:58px;line-height:66px}
.hero-title b{font-weight:900;display:block}
.hero-title span{font-weight:400;display:block}
.hero-sub{position:absolute;left:112px;top:412px;width:420px;color:var(--white);font-size:18px;line-height:26px;font-weight:500}
.slides{position:absolute;left:1046px;top:280px;width:100px;color:var(--white);text-align:right}
.slides .n{font-size:11px;margin-right:0;width:100%}
.slides .cur{display:flex;align-items:center;justify-content:flex-end;gap:12px;font-size:19px;font-weight:600;margin:6px 0}
.slides .cur i{display:block;width:64px;height:2px;background:var(--white)}

/* section titles */
.sec-title{position:absolute;left:0;width:1200px;text-align:center;font-size:40px;color:var(--brown);font-weight:400}
.sec-title b{font-weight:900}

/* services */
.svc{position:absolute;top:812px;width:296px;height:319px;border:1px solid var(--line);border-radius:6px;background:var(--page);text-align:center}
.svc.on{background:var(--orange-soft)}
.svc .ico{width:112px;height:112px;border-radius:50%;margin:36px auto 0;border:1px solid var(--line);background:radial-gradient(circle,#fbe9e2 0%,#f2d2c6 100%)}
.svc.on .ico{background:radial-gradient(circle,#f48a5f 0%,var(--orange) 100%);border:none}
.svc h3{color:var(--orange);font-weight:500;font-size:21px;margin-top:28px}
.svc p{font-size:13.5px;line-height:21px;color:var(--muted);padding:0 14px;margin-top:16px}

/* story */
.story{position:absolute;left:49px;top:1296px;width:1102px;height:507px;background:var(--brown);border-radius:10px}
.story-photo{position:absolute;left:63px;top:87px;width:446px;height:331px;border-radius:14px;background:linear-gradient(180deg,#b9c4cc 0%,#a3aab0 35%,#7e8682 60%,#5f6a5e 100%)}
.story h2{position:absolute;left:551px;top:78px;color:var(--white);font-size:38px;font-weight:400}
.story h2 b{font-weight:900}
.story p{position:absolute;left:551px;top:140px;width:476px;color:#f3e6e0;font-size:14.5px;line-height:25.8px;text-align:justify}
.story .btn{left:551px;top:384px;width:161px;height:36px}

/* testimonials */
.lead{position:absolute;left:190px;top:1958px;width:820px;text-align:center;font-size:16px;line-height:26px;color:var(--text)}
.quote{position:absolute;top:2056px;width:303px;height:306px;border:1px solid #7a3a28;border-radius:10px;background:var(--page);padding:20px 21px 0;overflow:hidden}
.quote .mark{display:block;height:40px}
.quote p{font-size:13.8px;line-height:21.5px;color:var(--muted);margin-top:12px;text-align:justify}
.quote .who{position:absolute;left:21px;top:234px;display:flex;align-items:center;gap:14px}
.avatar{width:52px;height:52px;border-radius:50%;background:linear-gradient(135deg,#c9b8ab,#8a6d5c)}
.who strong{display:block;font-weight:500;font-size:16px;color:var(--text)}
.dots{position:absolute;left:567px;top:2392px;display:flex;gap:8px}
.dots i{width:11px;height:11px;border-radius:50%;border:1.5px solid var(--orange)}
.dots i.on{background:var(--orange)}

/* supply band */
.band{position:absolute;left:0;top:2489px;width:1200px;height:510px;background:var(--band)}
.band h2{position:absolute;left:110px;top:84px;color:var(--brown);font-size:37px;line-height:45px;font-weight:400}
.band h2 b{font-weight:900;display:block}
.band p{position:absolute;left:614px;top:82px;width:476px;font-size:14.5px;line-height:25.8px;color:var(--muted);text-align:justify}

/* footer */
.footer{position:absolute;left:0;top:2998px;width:1200px;height:427px;background:linear-gradient(180deg,#6a2c16 0%,#5a2311 100%)}
.video{position:absolute;left:110px;top:2782px;width:979px;height:352px;border-radius:8px;background:linear-gradient(180deg,#a9c4e4 0%,#cdd3d8 45%,#e8b48a 72%,#2a1d18 73%,#1b1310 100%)}
.play{position:absolute;left:557px;top:2915px;width:86px;height:86px;border-radius:50%;background:var(--white);display:flex;align-items:center;justify-content:center}
.footer .brand{position:absolute;left:0;width:1200px;justify-content:center;top:220px}
.fnav{position:absolute;left:0;width:1200px;top:325px;display:flex;justify-content:center;gap:27px;color:var(--white);font-size:15px}
.frule{position:absolute;left:300px;top:361px;width:600px;height:1px;background:rgba(255,255,255,.35)}
.copy{position:absolute;left:0;width:1200px;top:380px;text-align:center;color:#f1dcd3;font-size:11.5px}
</style>
</head>
<body>

<header class="hero">
  <div class="hero-photo" role="img" aria-label="White semi truck with trailer driving on a highway"></div>
  <div class="brand"><span class="brand-dot"></span>Tvar Freight Global</div>
  <nav class="nav">
    <span class="active">Home</span>
    <span>Services ⌄</span>
    <span>Industries ⌄</span>
    <span>Request a Quote ⌄</span>
    <span>About Us</span>
    <span>Contact Us</span>
  </nav>
  <h1 class="hero-title"><b>DELIVERING</b><b>STRENGTH</b><span>IN EVERY MILE</span></h1>
  <p class="hero-sub">Secure and reliable transportation for all your cargo needs.</p>
  <a class="btn" style="left:112px;top:474px;width:160px;height:35px">Request A Quote</a>
  <div class="slides">
    <div class="n" style="padding-right:6px">01</div>
    <div class="cur"><i></i>02</div>
    <div class="n" style="padding-right:6px">03</div>
  </div>
</header>

<h2 class="sec-title" style="top:716px"><b>OUR</b> SERVICES</h2>

<div class="svc" style="left:112px">
  <div class="ico" role="img" aria-label="Flatbed truck icon"></div>
  <h3>Flatbed Transportation</h3>
  <p>From routine shipments to oversized and heavy-haul loads, we handle freight requiring proper securement,</p>
</div>
<div class="svc on" style="left:452px">
  <div class="ico" role="img" aria-label="Step deck truck icon"></div>
  <h3>Step Deck Transportation</h3>
  <p>Our step deck trucking services support tall, heavy, and specialized freight that requires additional</p>
</div>
<div class="svc" style="left:793px">
  <div class="ico" role="img" aria-label="Dry van truck icon"></div>
  <h3>Dry Van Transportation</h3>
  <p>From consumer goods to industrial materials, our dry van services provide the space, security,</p>
</div>
<a class="btn" style="left:520px;top:1175px;width:160px;height:36px">View More</a>

<section class="story">
  <div class="story-photo" role="img" aria-label="Line of white trucks on a highway from above"></div>
  <h2><b>OUR</b> STORY</h2>
  <p>Tvar Freight Global™ was born out of real-world experience in the fitness equipment industry. What started as a company shipping strength equipment, cardio machines, and training gear to gyms, schools, and commercial facilities quickly evolved into something bigger. As order volume grew and supply chains became more complex, the team developed deep expertise in co-ordinating freight, managing deliveries, and navigating the challenges of large-scale equipment transportation. That hands-on experience laid the foundation</p>
  <a class="btn">Learn More</a>
</section>

<h2 class="sec-title" style="top:1876px"><b>CUSTOMER</b> EXPERIENCES</h2>
<p class="lead">Lorem ipsum dolor sit amet, consectetur adipiscing elit, sed do eiusmod tempor incididunt ut labore et dolore magna aliqua. Quis ipsum suspendisse ultrices gravida.</p>

<div class="quote" style="left:-241px"><svg class="mark" width="40" height="30" viewBox="0 0 40 30"><path d="M0 12 Q2 2 16 0 V6 Q9 7 9 12 H16 V30 H0Z M22 12 Q24 2 38 0 V6 Q31 7 31 12 H38 V30 H22Z" fill="var(--orange)" opacity=".8"/></svg><p>“Lorem ipsum dolor sit amet, consectetur adipiscing elit, sed do eiusmod tempor incididunt ut labore et dolore magna aliqua. Quis ipsum suspendis ultrices gravida. Risus commodo viverra maecenas accumsan lacus vel fa cilisis.”</p></div>

<div class="quote" style="left:105px"><svg class="mark" width="40" height="30" viewBox="0 0 40 30"><path d="M0 12 Q2 2 16 0 V6 Q9 7 9 12 H16 V30 H0Z M22 12 Q24 2 38 0 V6 Q31 7 31 12 H38 V30 H22Z" fill="var(--orange)" opacity=".8"/></svg><p>“Lorem ipsum dolor sit amet, consectetur adipiscing elit, sed do eiusmod tempor incididunt ut labore et dolore magna aliqua. Quis ipsum suspendis ultrices gravida. Risus commodo viverra maecenas accumsan lacus vel fa cilisis.”</p>
  <div class="who"><div class="avatar" role="img" aria-label="Customer portrait"></div><div><strong>Marlo</strong><svg width="80" height="14" viewBox="0 0 80 14"><g fill="var(--star)"><polygon id="st" points="7,0 9,5 14,5 10,8 11.5,13 7,10 2.5,13 4,8 0,5 5,5"/><use href="#st" x="16"/><use href="#st" x="32"/><use href="#st" x="48"/><use href="#st" x="64"/></g></svg></div></div></div>

<div class="quote" style="left:449px"><svg class="mark" width="40" height="30" viewBox="0 0 40 30"><path d="M0 12 Q2 2 16 0 V6 Q9 7 9 12 H16 V30 H0Z M22 12 Q24 2 38 0 V6 Q31 7 31 12 H38 V30 H22Z" fill="var(--orange)" opacity=".8"/></svg><p>“Lorem ipsum dolor sit amet, consectetur adipiscing elit, sed do eiusmod tempor incididunt ut labore et dolore magna aliqua. Quis ipsum suspendis ultrices gravida. Risus commodo viverra maecenas accumsan lacus vel fa cilisis.”</p>
  <div class="who"><div class="avatar" role="img" aria-label="Customer portrait"></div><div><strong>Marlo</strong><svg width="80" height="14" viewBox="0 0 80 14"><g fill="var(--star)"><use href="#st"/><use href="#st" x="16"/><use href="#st" x="32"/><use href="#st" x="48"/><use href="#st" x="64"/></g></svg></div></div></div>

<div class="quote" style="left:793px"><svg class="mark" width="40" height="30" viewBox="0 0 40 30"><path d="M0 12 Q2 2 16 0 V6 Q9 7 9 12 H16 V30 H0Z M22 12 Q24 2 38 0 V6 Q31 7 31 12 H38 V30 H22Z" fill="var(--orange)" opacity=".8"/></svg><p>“Lorem ipsum dolor sit amet, consectetur adipiscing elit, sed do eiusmod tempor incididunt ut labore et dolore magna aliqua. Quis ipsum suspendis ultrices gravida. Risus commodo viverra maecenas accumsan lacus vel fa cilisis.”</p>
  <div class="who"><div class="avatar" role="img" aria-label="Customer portrait"></div><div><strong>Marlo</strong><svg width="80" height="14" viewBox="0 0 80 14"><g fill="var(--star)"><use href="#st"/><use href="#st" x="16"/><use href="#st" x="32"/><use href="#st" x="48"/><use href="#st" x="64"/></g></svg></div></div></div>

<div class="quote" style="left:1139px"><svg class="mark" width="40" height="30" viewBox="0 0 40 30"><path d="M0 12 Q2 2 16 0 V6 Q9 7 9 12 H16 V30 H0Z M22 12 Q24 2 38 0 V6 Q31 7 31 12 H38 V30 H22Z" fill="var(--orange)" opacity=".8"/></svg><p>“Lorem ipsum dolor sit amet, consectetur adipiscing elit, sed do eiusmod tempor incididunt ut labore et dolore magna aliqua. Quis ipsum suspendis ultrices gravida. Risus commodo viverra maecenas accumsan lacus vel fa cilisis.”</p>
  <div class="who"><div class="avatar" role="img" aria-label="Customer portrait"></div></div></div>

<div class="dots"><i class="on"></i><i></i><i></i><i></i></div>

<section class="band">
  <h2><b>KEEPING YOUR SUPPLY</b>CHAIN MOVING</h2>
  <p>We deliver a comprehensive range of open-deck and specialized transportation services—including flatbed, step deck, heavy haul, and over-dimensional freight solutions. Backed by years of experience, a trusted nationwide carrier network, and a strong safety-first culture, we provide reliable, adaptable logistics support built around the unique requirements of every load.</p>
</section>

<footer class="footer">
  <div class="brand"><span class="brand-dot"></span>Tvar Freight Global</div>
  <nav class="fnav"><span>Home</span><span>Services</span><span>Industries</span><span>Request a Quote</span><span>About Us</span><span>Contact Us</span></nav>
  <div class="frule"></div>
  <p class="copy">Copyright © 2026 Tvar Freight Global™. All rights reserved.</p>
</footer>

<div class="video" role="img" aria-label="Video still: workers loading boxes into a truck at sunset, in silhouette"></div>
<div class="play"><svg width="30" height="34" viewBox="0 0 30 34"><polygon points="4,0 30,17 4,34" fill="var(--orange)"/></svg></div>

</body>
</html>
```